environmentalist needs a bumper sticker design

The bumper sticker should say, "There is no Planet B."

thank you for the designs so far. Some have asked for more direction of my thinking. You've probably heard people talk of "Plan A" and "Plan B" when they want to consider alternatives. "There is no Planet B" reminds us that there are no alternatives. The question is, how best to encourage people to act? Research indicates that making people fearful is less effective (although certainly we have plenty to fear). It is more effective to stir emotions of caring and attachment. For example, designs that show the earth as a beautiful planet, or aspects of the earth (e.g., trees and mountains or whatever) remind us of what we love and want to care for.

```html
<!DOCTYPE html>
<html lang="en">
<head>
<meta charset="UTF-8">
<title>There Is NO Planet B – Bumper Sticker</title>
<link rel="stylesheet" href="https://fonts.googleapis.com/css2?family=Tenor+Sans&display=swap">
<style>
  :root {
    --page-bg: #ffffff;
    --sticker-bg: #000000;
    --text-light: #ffffff;
    --text-accent: #e3171f;
    --globe-core: #1f72b8;
    --globe-mid: #2456a6;
    --globe-edge: #2b3889;
  }
  html, body {
    margin: 0;
    padding: 0;
    width: 1200px;
    height: 1000px;
    overflow: hidden;
    background: var(--page-bg);
  }
  .canvas {
    position: relative;
    width: 1200px;
    height: 1000px;
  }
  .sticker {
    position: absolute;
    left: 186px;
    top: 368px;
    width: 829px;
    height: 270px;
  }
  .slogan {
    font-family: "Tenor Sans", "Optima", sans-serif;
    font-size: 70px;
    letter-spacing: 0;
    fill: var(--text-light);
  }
  .slogan-accent {
    fill: var(--text-accent);
  }
</style>
</head>
<body>
<div class="canvas">
  <svg class="sticker" viewBox="186 368 829 270" width="829" height="270" xmlns="http://www.w3.org/2000/svg">
    <defs>
      <clipPath id="sticker-clip">
        <rect x="186" y="368" width="829" height="270"/>
      </clipPath>
      <radialGradient id="globe-fill" cx="600" cy="640" r="520" gradientUnits="userSpaceOnUse">
        <stop offset="0" stop-color="var(--globe-core)"/>
        <stop offset="0.6" stop-color="var(--globe-mid)"/>
        <stop offset="1" stop-color="var(--globe-edge)"/>
      </radialGradient>
      <path id="slogan-arc" d="M190 560 A832 832 0 0 1 1010 560"/>
    </defs>

    <rect class="sticker-bg" x="186" y="368" width="829" height="270" fill="var(--sticker-bg)"/>

    <g clip-path="url(#sticker-clip)">
      <ellipse class="globe" role="img" aria-label="Blue planet Earth seen from space with green continents"
               cx="600" cy="900" rx="520" ry="433" fill="url(#globe-fill)"/>
    </g>

    <text class="slogan">
      <textPath href="#slogan-arc" startOffset="50%" text-anchor="middle" textLength="770" lengthAdjust="spacingAndGlyphs">There Is <tspan class="slogan-accent">NO</tspan> Planet B</textPath>
    </text>
  </svg>
</div>
</body>
</html>
```